Real Estate Business card design

Company Name: Tamarind Holdings, LLC
subtitle: We pay cash for houses!
Daniel Whitcombe
Managing Director
555-214-0963
Dan@TamarindHoldingsLLC.example
www.TamarindHoldingsLLC.example

We pay referral fees for Seller and Buyer leads.

Back:
We offer referral fees for Seller and Buyer leads that close.

Please contact Hal at 555-214-0963 with your referrals or to learn more about the referral program!

I am open to different color options but I am going for a classic, elegant, clean, and professional look. Please use logo as a reference.

Target Market(s)

People selling their homes and people in the market for buying homes.

Contact Information for Business Card

please see project description

Font styles to use
Serif
Sans Serif
Script

Requirements
Must have
• must have my logo in it
Nice to have
• I like cards that are split down the middle but please come up with a few mock ups. Open to any color scheme.

```html
<!DOCTYPE html>
<html lang="en">
<head>
<meta charset="utf-8">
<title>Tamarind Holdings, LLC — Business Card</title>
<link rel="stylesheet" href="https://fonts.googleapis.com/css2?family=Lato:ital,wght@0,400;0,700;0,900;1,400;1,700&display=swap">
<style>
  :root {
    --stage: #2b2b2d;
    --tan: #c59c76;
    --tan-deep: #b98c63;
    --paper: #f3f1f2;
    --slate: #474e59;
    --slate-ink: #35404e;
    --white: #ffffff;
  }
  * { box-sizing: border-box; margin: 0; padding: 0; }
  html, body {
    width: 1200px; height: 1015px; overflow: hidden;
    background: var(--stage);
    font-family: "Lato", sans-serif;
  }
  .sheet {
    width: 1200px; height: 1015px;
    display: flex; flex-direction: column; align-items: center; justify-content: center;
    gap: 60px;
  }
  .card {
    width: 700px; height: 400px; position: relative; overflow: hidden;
    box-shadow: 0 14px 30px rgba(0,0,0,.45);
  }

  /* Tan side */
  .card--cash { background: var(--tan); }
  .cash__texture {
    position: absolute; inset: 0;
    background: linear-gradient(135deg, var(--tan) 0%, var(--tan-deep) 100%);
  }
  .cash__content {
    position: absolute; inset: 0;
    display: flex; align-items: center; justify-content: center; gap: 48px;
  }
  .cash__brand {
    display: flex; align-items: center; gap: 10px;
    color: var(--white); font-weight: 700; font-size: 30px; letter-spacing: .5px;
  }
  .cash__brand .mark { width: 12px; height: 12px; background: var(--white); }
  .cash__tagline { color: var(--white); font-weight: 900; font-size: 24px; }

  /* Contact side */
  .card--contact { background: var(--paper); }
  .contact__top { position: absolute; left: 0; right: 0; top: 0; height: 228px; }
  .contact__person { position: absolute; left: 56px; top: 86px; }
  .contact__name {
    color: var(--tan); font-weight: 700; font-size: 26px; letter-spacing: .5px;
    text-transform: uppercase; margin-bottom: 22px;
  }
  .contact__list { list-style: none; color: var(--slate-ink); font-size: 17px; line-height: 1.45; }
  .contact__list li { display: flex; align-items: center; gap: 10px; }
  .contact__list svg { width: 15px; height: 15px; flex: none; }
  .contact__brand {
    position: absolute; right: 46px; top: 70px; text-align: left;
    display: flex; align-items: center; gap: 12px;
    color: var(--slate-ink); font-weight: 700; font-size: 38px; line-height: 1.05;
  }
  .contact__brand .mark { width: 16px; height: 16px; background: var(--tan); flex: none; }
  .contact__band {
    position: absolute; left: 0; right: 0; top: 228px; height: 34px;
    background: var(--tan); color: var(--white);
    display: flex; align-items: center; justify-content: flex-end; padding-right: 46px;
    font-style: italic; font-size: 17px;
  }
  .contact__rule { position: absolute; left: 0; right: 0; top: 262px; height: 5px; background: var(--paper); }
  .contact__referral {
    position: absolute; left: 0; right: 0; top: 267px; bottom: 0;
    background: var(--slate); color: var(--white);
    display: flex; flex-direction: column; align-items: center; justify-content: center;
    text-align: center; font-size: 16px; line-height: 1.45; padding: 0 60px;
  }
  .contact__referral p + p { margin-top: 6px; }
  .contact__referral strong { font-weight: 900; }
</style>
</head>
<body>
<main class="sheet">
  <section class="card card--cash">
    <div class="cash__texture" role="img" aria-label="Embossed repeating pattern of the company mark on tan stock"></div>
    <div class="cash__content">
      <div class="cash__brand"><span class="mark"></span>Tamarind</div>
      <div class="cash__tagline">We pay cash for houses!</div>
    </div>
  </section>

  <section class="card card--contact">
    <div class="contact__top">
      <div class="contact__person">
        <h1 class="contact__name">Daniel Whitcombe</h1>
        <ul class="contact__list">
          <li>
            <svg viewBox="0 0 24 24" fill="var(--tan)"><path d="M6.6 10.8a15.1 15.1 0 0 0 6.6 6.6l2.2-2.2c.3-.3.7-.4 1-.2 1.1.4 2.3.6 3.6.6.6 0 1 .4 1 1V20c0 .6-.4 1-1 1A17 17 0 0 1 3 4c0-.6.4-1 1-1h3.5c.6 0 1 .4 1 1 0 1.3.2 2.5.6 3.6.1.3 0 .7-.2 1z"/></svg>
            555-214-0963
          </li>
          <li>
            <svg viewBox="0 0 24 24" fill="var(--tan)"><path d="M2 5h20v14H2z" opacity=".9"/><path d="M2 5l10 8 10-8" stroke="var(--paper)" stroke-width="2" fill="none"/></svg>
            Dan@TamarindHoldingsLLC.example
          </li>
          <li>
            <svg viewBox="0 0 24 24" fill="none" stroke="var(--tan)" stroke-width="2"><circle cx="12" cy="12" r="10"/><path d="M2 12h20M12 2c3 3 3 17 0 20M12 2c-3 3-3 17 0 20"/></svg>
            www.TamarindHoldingsLLC.example
          </li>
        </ul>
      </div>
      <div class="contact__brand"><span class="mark"></span><span>Tamarind<br>Holdings, LLC</span></div>
    </div>
    <div class="contact__band">We pay referral fees for Seller and Buyer leads</div>
    <div class="contact__rule"></div>
    <div class="contact__referral">
      <p>We offer referral fees for Seller and Buyer leads that close.</p>
      <p>Please contact <strong>Hal</strong> at <strong>555-214-0963</strong> with<br>your referrals or to learn more about the referral program!</p>
    </div>
  </section>
</main>
</body>
</html>
```